Exciting Poster Project: 4 posters for Employee Benefit Program

We are an entrepreneurial healthcare IT company that is creating an internal campaign to launch our 2017 Culture and Professional Development goals for our internal staff.

We need 4 posters utilizing the 4 campaign logos (attached) that are tied together visually into a cohesive campaign.

A PPT is included that shows the other wall art that currently exists on the walls. The new posters will share a space with these pieces.

The posters may be mounted side by side, or stand alone on a wall- so the design should work both ways. Each poster should include its own icon and the tag line provided along with topics provided that fall under this category. The posters size can be dictated by your design, but the text should be legible from a minimum of 8 feet away.

At the bottom of each poster should include all 4 icons in order to tie the entire campaign together (perhaps they can be arranged together like a diamond shape with the primary one as the biggest diamond)

Our company website for our external branding is: www.quillmarsh.com
We have included our branding guidelines for our external brand, and ppts and graphics for our internal brand.

1) Poster 1:
a. Header: Better Today Than Yesterday
b. Sub-title: Personal and Professional Growth
c. Description: We are committed to helping you build on your strengths and passions and support you your career advancement goals. We have a variety of training and development programs available to help you reach your top potential!
Leadership Development Programs
1. Supervisor Training
2. Women’s Leadership
3. Leadership Meet-Ups
4. MBA Program
Staff Development
1. Continuing Education Fund
2. Book Club
3. Quillmarsh University
4. Mentorship
5. Learning Libraries
6. Department Wide Training Events

2) Poster 2:
a. Header: Perform at Highest Capacity
b. Sub-title: Be Your Best Self
c. Description: We are committed to providing programs that bring focus to your health and overall personal wellness to encourage a well balanced life
i. Healthy Living
1. Health and wellness seminars
2. Nutrition: Fruit Delivery
ii. Fitness:
1. Step Challenge
2. Virtual 5k
3. Recess
4. Golf Lessons
5. Ping Pong Club
iii. Creativity:
1. Painting
2. Photography Club
3. Virtual Trivia
iv. Mental Health:
1. Massage Therapy
2. EAP Education
v. Financial
1. 401(k)
2. Retirement education/financial planning seminars
3. Global Insurance Program education

3) Poster 3:
a. Header: Passionate Urgent and Driven to Success
b. Sub-Header: Innovation and Strategy
c. Description: We are committed to helping you connect the dots both in the industry and with our internal goals , mission, and vision.
i. Quarterly All-Hands
ii. LoopTalk
1. Internally: Departmental and Product Updates
2. Externally: Industry Knowledge
3. Culturally: Peer to Peer Community

4) Poster 4:
a. Header: Succeed as a Team
b. Sub-Header: Cultivating Collaboration
c. Description: We are committed to creating a culture of appreciation, teamwork, and supporting an open communication. All feedback and ideas are welcome here!
i. Team Building Events
1. Employee Focused
a. Summer Picnic
b. Employee Appreciation
c. Diwali
d. Holiday Party
e. Department Appreciation
2. Family Friendly
a. Halloween
b. Bring your Kids to Work Day
3. Awards
a. Peer to Peer: BrightNod Awards
b. Leadership: Crest of Merit
4. Surveys
a. New Hire
b. Employee Engagement
Updates

Target Market(s)

Internal Employees

Industry/Entity Type

Healthcare

Font styles to use
Sans Serif

Requirements
Must have
• Job Type: Posters
• Task Outline: Create Vector Art for 4 icons and 4 posters
• Fonts and Styles to Use: SourceSansPro
Nice to have
• There is an attachment with suggested concepts and styles that we like.
Should not have
• The poster should not be very wordy or hard to read in passing.

```html
<!DOCTYPE html>
<html lang="en">
<head>
<meta charset="utf-8">
<title>Succeed as a Team – Cultivating Collaboration</title>
<link href="https://fonts.googleapis.com/css2?family=Source+Sans+3:wght@300;400;600;700&display=swap" rel="stylesheet">
<style>
  :root{
    --gold:#C8914E;
    --white:#FFFFFF;
    --grey-text:#9A9EA4;
    --orange:#E8943A;
    --red-a:#E94B3A;
    --red-b:#E51D37;
    --blue-a:#3A7FC3;
    --blue-b:#434C9E;
    --crimson:#A51D32;
    --green-a:#90C640;
    --green-b:#8BBE3F;
    --navy:#1E2E5E;
    --mark:#F26B2A;
  }
  *{margin:0;padding:0;box-sizing:border-box;}
  html,body{width:849px;height:1200px;overflow:hidden;}
  body{font-family:"Source Sans 3",sans-serif;}
  .poster{
    position:relative;width:849px;height:1200px;overflow:hidden;
    background:radial-gradient(ellipse 70% 55% at 50% 55%,#F6F6F7 0%,#E3E5E8 55%,#B6BDC5 100%);
  }
  .headline{
    position:absolute;top:38px;left:0;width:100%;text-align:center;
    color:var(--gold);font-weight:600;font-size:104px;letter-spacing:-5px;line-height:1;
    white-space:nowrap;transform:scaleX(.83);transform-origin:50% 0;
  }
  .subhead{
    position:absolute;top:142px;left:0;width:100%;text-align:center;
    color:var(--white);font-weight:400;font-size:53px;line-height:1;letter-spacing:.5px;
  }
  .tile{position:absolute;width:335px;height:335px;color:var(--white);padding:28px 30px;}
  .tile h2{font-size:38px;line-height:1.04;font-weight:700;letter-spacing:-.6px;}
  .tile h2 span{display:block;font-weight:400;}
  .tile ul{list-style:none;margin-top:12px;font-size:28.5px;line-height:38.5px;letter-spacing:-.9px;white-space:nowrap;}
  .tile--employee{left:82px;top:226px;border-radius:18px 95px 0 95px;
    background:linear-gradient(135deg,var(--red-a),var(--red-b));}
  .tile--family{left:433px;top:226px;border-radius:95px 0 95px 0;text-align:right;
    background:linear-gradient(135deg,var(--blue-a),var(--blue-b));}
  .tile--family ul{margin-right:-4px;}
  .tile--awards{left:82px;top:583px;border-radius:95px 0 95px 0;background:var(--crimson);padding-top:56px;}
  .tile--surveys{left:433px;top:583px;border-radius:0 95px 0 95px;text-align:right;padding-top:56px;
    background:linear-gradient(135deg,var(--green-a),var(--green-b));}
  .tile--awards ul,.tile--surveys ul{margin-top:36px;}
  .tile--family ul{margin-top:14px;}
  .statement{
    position:absolute;top:932px;left:0;width:100%;text-align:center;
    color:var(--grey-text);font-weight:300;font-size:33.5px;line-height:41px;letter-spacing:-.3px;
    white-space:nowrap;
  }
  .statement strong{display:block;color:var(--orange);font-weight:400;}
  .brand{
    position:absolute;top:1090px;left:204px;display:flex;align-items:center;gap:18px;
  }
  .brand-square{width:58px;height:58px;background:var(--mark);border-radius:6px;}
  .brand-name{color:var(--navy);font-weight:700;font-size:46px;letter-spacing:-1.5px;line-height:1;}
  .campaign-icons{
    position:absolute;left:540px;top:1071px;width:94px;height:94px;
  }
</style>
</head>
<body>
<main class="poster">
  <h1 class="headline">SUCCEED AS A TEAM</h1>
  <p class="subhead">Cultivating Collaboration</p>

  <section class="tile tile--employee">
    <h2>EMPLOYEE<span>FOCUSED</span></h2>
    <ul>
      <li>Summer Picnic</li>
      <li>Employee Appreciation</li>
      <li>Diwali</li>
      <li>Holiday Party</li>
    </ul>
  </section>

  <section class="tile tile--family">
    <h2>FAMILY<span>FRIENDLY</span></h2>
    <ul>
      <li>Halloween</li>
      <li>Bring your Kids to Work</li>
      <li>Day</li>
    </ul>
  </section>

  <section class="tile tile--awards">
    <h2>AWARDS</h2>
    <ul>
      <li>Peer to Peer:</li>
      <li>BrightNod Awards</li>
      <li>Leadership: Crest of</li>
      <li>Merit</li>
    </ul>
  </section>

  <section class="tile tile--surveys">
    <h2>SURVEYS</h2>
    <ul>
      <li>New Hire</li>
      <li>Employee Engagement</li>
    </ul>
  </section>

  <p class="statement">We are committed to creating a culture of appreciation,<br>teamwork, and supporting an open communication.
    <strong>All feedback and ideas are welcome here!</strong></p>

  <div class="brand">
    <span class="brand-square"></span>
    <span class="brand-name">Quillmarsh</span>
  </div>

  <svg class="campaign-icons" viewBox="0 0 96 96" role="img" aria-label="Cluster of the four campaign icons arranged in a diamond">
    <defs>
      <linearGradient id="campaignTones" x1="0" y1="0" x2="1" y2="1">
        <stop offset="0" stop-color="#D9A35A"/>
        <stop offset=".35" stop-color="#7B4A9A"/>
        <stop offset=".7" stop-color="#3B8E97"/>
        <stop offset="1" stop-color="#86B843"/>
      </linearGradient>
    </defs>
    <rect x="0" y="0" width="96" height="96" rx="10" fill="url(#campaignTones)" opacity=".55"/>
  </svg>
</main>
</body>
</html>
```